Brisk & Halloway Solar Interior Wall Covering

We would like designs for internal showroom wall design for Brisk & Halloway solar.

Using elements from the attached flyer

Dimensions are 5830mm (W) x 2880mm (H)

```html
<!DOCTYPE html>
<html lang="en">
<head>
<meta charset="utf-8">
<title>Brisk &amp; Halloway Solar – Showroom Wall</title>
<link rel="stylesheet" href="https://fonts.googleapis.com/css2?family=Arimo:wght@400;700&display=swap">
<style>
  :root {
    --navy: #0d3a7e;
    --orange: #f5a21b;
    --orange-deep: #ee8a12;
    --white: #ffffff;
    --page: #eeeeee;
    --divider: rgba(255,255,255,0.35);
  }
  html, body {
    margin: 0;
    padding: 0;
    width: 1200px;
    height: 1200px;
    overflow: hidden;
    background: var(--page);
    font-family: "Arimo", Arial, sans-serif;
  }
  .wall {
    position: absolute;
    left: 40px;
    top: 323px;
    width: 1120px;
    height: 553px;
    background: var(--navy);
    overflow: hidden;
  }
  .wall__art {
    position: absolute;
    inset: 0;
  }
  .brand {
    position: absolute;
    left: 68px;
    top: 64px;
    display: flex;
    align-items: center;
    gap: 16px;
  }
  .brand__dot {
    width: 44px;
    height: 44px;
    border-radius: 50%;
    background: var(--orange);
  }
  .brand__name {
    color: var(--white);
    font-weight: 700;
    font-size: 34px;
    letter-spacing: 1px;
    text-transform: uppercase;
  }
  .web-band {
    position: absolute;
    left: 554px;
    top: 88px;
    width: 566px;
    height: 41px;
    background: var(--orange);
    color: var(--white);
    font-weight: 700;
    font-size: 28px;
    line-height: 41px;
    text-align: center;
  }
  .benefit {
    position: absolute;
    width: 180px;
    margin-left: -90px;
    text-align: center;
    color: var(--white);
    font-size: 18px;
    line-height: 22px;
    text-transform: uppercase;
  }
  .benefit svg {
    display: block;
    margin: 0 auto 8px;
  }
  .divider {
    position: absolute;
    width: 1px;
    background: var(--divider);
  }
</style>
</head>
<body>
<main class="wall">
  <svg class="wall__art" width="1120" height="553" viewBox="0 0 1120 553">
    <defs>
      <radialGradient id="sunGlow" cx="1066" cy="428" r="520" gradientUnits="userSpaceOnUse">
        <stop offset="0" stop-color="#f5a21b" stop-opacity="1"/>
        <stop offset="0.28" stop-color="#f5a21b" stop-opacity="0.85"/>
        <stop offset="1" stop-color="#f5a21b" stop-opacity="0"/>
      </radialGradient>
    </defs>
    <polygon class="white-field" points="602,553 1120,0 1120,553" fill="#ffffff"/>
    <rect class="sun-decoration" x="560" y="0" width="560" height="553" fill="url(#sunGlow)" role="img" aria-label="Large orange sun with rays rising from the lower right corner"/>
  </svg>

  <div class="brand">
    <span class="brand__dot"></span>
    <span class="brand__name">Brisk &amp; Halloway</span>
  </div>

  <div class="web-band">Briskhallowaysolar.com.au</div>

  <div class="divider" style="left:209px; top:248px; height:103px;"></div>
  <div class="divider" style="left:396px; top:248px; height:103px;"></div>
  <div class="divider" style="left:209px; top:402px; height:103px;"></div>
  <div class="divider" style="left:396px; top:402px; height:103px;"></div>

  <div class="benefit" style="left:125px; top:233px;">
    <svg width="66" height="66" viewBox="0 0 66 66"><circle cx="33" cy="33" r="31" fill="none" stroke="#f5a21b" stroke-width="2.5"/><rect x="22" y="16" width="22" height="30" rx="2" fill="#f5a21b"/><text x="33" y="38" text-anchor="middle" font-family="Arimo, sans-serif" font-weight="700" font-size="18" fill="#0d3a7e">$</text><path d="M28 48 L33 53 L38 48" fill="none" stroke="#f5a21b" stroke-width="3"/></svg>
    Save on your<br>power bills
  </div>
  <div class="benefit" style="left:300px; top:233px;">
    <svg width="66" height="66" viewBox="0 0 66 66"><circle cx="33" cy="33" r="31" fill="none" stroke="#f5a21b" stroke-width="2.5"/><circle cx="33" cy="33" r="17" fill="#f5a21b"/><g fill="none" stroke="#0d3a7e" stroke-width="2"><ellipse cx="33" cy="33" rx="7" ry="17"/><line x1="16" y1="33" x2="50" y2="33"/><line x1="19" y1="25" x2="47" y2="25"/><line x1="19" y1="41" x2="47" y2="41"/></g></svg>
    Good for the<br>environment
  </div>
  <div class="benefit" style="left:492px; top:233px;">
    <svg width="66" height="66" viewBox="0 0 66 66"><circle cx="33" cy="33" r="31" fill="none" stroke="#f5a21b" stroke-width="2.5"/><rect x="18" y="22" width="14" height="14" rx="2" fill="#f5a21b"/><line x1="21" y1="15" x2="21" y2="22" stroke="#f5a21b" stroke-width="3"/><line x1="29" y1="15" x2="29" y2="22" stroke="#f5a21b" stroke-width="3"/><path d="M25 36 Q25 50 38 48" fill="none" stroke="#f5a21b" stroke-width="3"/><path d="M42 22 Q50 30 46 38 Q42 42 38 38 Q36 30 42 22Z" fill="#f5a21b"/></svg>
    Connect to<br>the grid
  </div>

  <div class="benefit" style="left:125px; top:386px;">
    <svg width="66" height="66" viewBox="0 0 66 66"><circle cx="33" cy="33" r="31" fill="none" stroke="#f5a21b" stroke-width="2.5"/><path d="M33 16 Q44 30 44 38 A11 11 0 0 1 22 38 Q22 30 33 16Z" fill="#f5a21b"/></svg>
    Low<br>maintenance
  </div>
  <div class="benefit" style="left:300px; top:386px;">
    <svg width="66" height="66" viewBox="0 0 66 66"><circle cx="33" cy="33" r="31" fill="none" stroke="#f5a21b" stroke-width="2.5"/><circle cx="33" cy="33" r="12" fill="#f5a21b"/><g stroke="#f5a21b" stroke-width="2.5"><line x1="33" y1="10" x2="33" y2="16"/><line x1="33" y1="50" x2="33" y2="56"/><line x1="10" y1="33" x2="16" y2="33"/><line x1="50" y1="33" x2="56" y2="33"/><line x1="17" y1="17" x2="21" y2="21"/><line x1="45" y1="45" x2="49" y2="49"/><line x1="49" y1="17" x2="45" y2="21"/><line x1="17" y1="49" x2="21" y2="45"/></g><path d="M35 24 L28 35 L33 35 L30 43 L38 31 L33 31Z" fill="#0d3a7e"/></svg>
    Government<br>subsidies
  </div>
  <div class="benefit" style="left:492px; top:386px;">
    <svg width="66" height="66" viewBox="0 0 66 66"><circle cx="33" cy="33" r="31" fill="none" stroke="#f5a21b" stroke-width="2.5"/><path d="M26 22 Q26 14 33 14 Q40 14 40 22" fill="none" stroke="#f5a21b" stroke-width="3"/><rect x="20" y="22" width="26" height="26" rx="3" fill="#f5a21b"/><text x="33" y="41" text-anchor="middle" font-family="Arimo, sans-serif" font-weight="700" font-size="16" fill="#0d3a7e">$</text></svg>
    Add value to<br>your property
  </div>
</main>
</body>
</html>
```